Law Firm Letterhead

We are looking for a letterhead for our military/veterans law firm. We like simplicity and clean, modern, flat, uncluttered designs. Our logo font is DIN 1451, and our website/business card info font is Helvetica Neue.

Required Information:

- Logo/Graphic: Please see attached logo / business card for ideas. Please also review firm website.

- Motto: A law firm for service members and veterans

- Web Address: www.brightharborcounsel.example

- Email: info@brightharborcounsel.example

- Phone: 866-214-3097

Colors: We prefer either a blue/grey or an all-blue color scheme. The blue in our logo is #336699.

Please DO NOT submit more than 3 designs. Spamming designs with only minor changes between the designs is not appreciated. We can evaluate your quality and direction by your best 1 or 2 designs.

Thank you!

```html
<!DOCTYPE html>
<html lang="en">
<head>
<meta charset="utf-8">
<title>Bright Harbor Counsel – Letterhead</title>
<link href="https://fonts.googleapis.com/css2?family=Arimo:wght@400;500&family=Barlow+Condensed:wght@500;600&display=swap" rel="stylesheet">
<style>
  :root {
    --brand-blue: #2a6cc4;
    --ink: #3a3a3a;
    --paper: #ffffff;
    --backdrop: #e9ebee;
  }
  * { box-sizing: border-box; margin: 0; padding: 0; }
  html, body {
    width: 1200px;
    height: 923px;
    overflow: hidden;
    background: var(--backdrop);
  }
  .canvas {
    position: relative;
    width: 1200px;
    height: 923px;
  }
  .letterhead {
    position: absolute;
    left: 264px;
    top: 22px;
    width: 672px;
    height: 879px;
    background: var(--paper);
    box-shadow: 0 2px 10px rgba(0, 0, 0, 0.12);
    font-family: "Arimo", "Helvetica Neue", Arial, sans-serif;
  }
  .firm-name {
    position: absolute;
    top: 40px;
    left: 0;
    width: 672px;
    text-align: center;
    font-family: "Barlow Condensed", "DIN 1451", sans-serif;
    font-weight: 600;
    font-size: 34px;
    letter-spacing: 1px;
    line-height: 1;
    color: var(--brand-blue);
    text-transform: uppercase;
  }
  .sender {
    position: absolute;
    top: 96px;
    right: 30px;
    text-align: right;
    color: var(--ink);
  }
  .sender-name {
    font-size: 16px;
    font-weight: 500;
    color: var(--brand-blue);
    line-height: 1.2;
  }
  .sender-title {
    font-size: 11.5px;
    margin-top: 2px;
    letter-spacing: 0.3px;
  }
  .sender-contact {
    list-style: none;
    margin-top: 8px;
    font-size: 8px;
    line-height: 1.5;
  }
  .contact-label {
    color: var(--brand-blue);
    font-weight: 500;
    margin-right: 4px;
  }
  .footer {
    position: absolute;
    bottom: 34px;
    left: 0;
    width: 672px;
    text-align: center;
  }
  .motto {
    font-size: 14px;
    color: var(--brand-blue);
    letter-spacing: 0.2px;
  }
  .web-address {
    font-size: 10px;
    color: var(--ink);
    margin-top: 1px;
  }
</style>
</head>
<body>
  <main class="canvas">
    <section class="letterhead">
      <h1 class="firm-name">Bright Harbor Counsel</h1>

      <address class="sender" style="font-style: normal;">
        <p class="sender-name">Daniel Mercer</p>
        <p class="sender-title">Attorney / Owner</p>
        <ul class="sender-contact">
          <li><span class="contact-label">p</span>866-214-3097</li>
          <li><span class="contact-label">e</span>daniel.mercer@brightharborcounsel.example</li>
        </ul>
      </address>

      <footer class="footer">
        <p class="motto">a law firm for service members and veterans</p>
        <p class="web-address">www.brightharborcounsel.example</p>
      </footer>
    </section>
  </main>
</body>
</html>
```